Brightfold Business Cards

Two types of business cards:
square and rectangle.

Contact Information for Business Card

SQUARE
Square versions will not be specific to a person and will just have the clinic information on them. I'd like to have 4-5 options for printing on the back. I am using pexlo-print.example, and with that service you can upload multiple designs for the backs of the cards. So - same generic design on the front and different full color pictures with logo integration on the back. We have not selected final photos yet, but I will upload a couple to use for mock-ups.

RECTANGLE
These will be specific to providers. I would like to be able to switch out the name, title, and email address on my own (I can use photoshop or illustrator to do this) so that when we get new providers it is quick to get them cards. The rectangle cards could have multiple designs on the back as well. I am uploading examples of our OLD cards with our OLD logo.

Current logo will be uploaded as well.

I will upload high res photos to use as well as the setup template from the printer.

Font styles to use
Other font styles liked:
• Mayeka Demi Bold (logo); Questrial; open to other font choices

Colors
0455a3
9bcb3b

Requirements
Must have
• Blue - 654C
• Green - 376C
• Font on logo: Mayeka Demi Bold
• Other font I like: Questrial
• Open to other font choices as well.

```html
<!DOCTYPE html>
<html lang="en">
<head>
<meta charset="utf-8">
<title>Brightfold Chiropractic – Square Cards</title>
<link rel="stylesheet" href="https://fonts.googleapis.com/css2?family=Questrial&display=swap">
<style>
  :root {
    --canvas: #ececec;
    --navy: #1b3c6a;
    --green: #8dc63f;
    --white: #ffffff;
    --ink: #1d1d1d;
    --sunset-top: #e9894f;
    --sunset-mid: #e86a3a;
    --sea: #6a5660;
    --dusk-top: #f0a45a;
    --dusk-mid: #d9573a;
    --dusk-low: #a4566a;
    --dusk-deep: #2c2a45;
  }
  * { box-sizing: border-box; margin: 0; padding: 0; }
  html, body { width: 1200px; height: 1000px; overflow: hidden; }
  body {
    background: var(--canvas);
    font-family: "Questrial", Arial, sans-serif;
    position: relative;
  }
  .card {
    position: absolute;
    width: 358px;
    height: 360px;
    overflow: hidden;
  }
  .card--front-a { left: 164px; top: 104px; }
  .card--back-sea { left: 657px; top: 104px; }
  .card--back-beach { left: 162px; top: 528px; }
  .card--front-b { left: 656px; top: 528px; }

  /* Front layout */
  .front { display: flex; background: var(--white); }
  .front__band {
    width: 134px;
    height: 100%;
    background: var(--navy);
    position: relative;
  }
  .front__name {
    position: absolute;
    left: 50%;
    top: 50%;
    transform: translate(-50%, -50%) rotate(-90deg);
    white-space: nowrap;
    color: var(--white);
    font-size: 17px;
    letter-spacing: 3px;
    text-transform: uppercase;
  }
  .front__info {
    flex: 1;
    text-align: center;
    color: var(--ink);
    padding-top: 49px;
  }
  .services { list-style: none; font-size: 11px; line-height: 19.5px; text-transform: uppercase; }
  .rule {
    width: 102px;
    height: 2px;
    margin: 17px auto 20px;
    background: var(--green);
    border-radius: 1px;
  }
  .address, .contact { font-size: 12px; line-height: 16.5px; }
  .contact { line-height: 19px; }
  .rule--second { margin-top: 21px; margin-bottom: 16px; }

  /* Backs */
  .photo { position: absolute; inset: 0; }
  .photo--sea {
    background: linear-gradient(180deg, #f0a98a 0%, var(--sunset-top) 25%, var(--sunset-mid) 52%, #c86a48 62%, var(--sea) 85%, #4a4a55 100%);
  }
  .photo--beach {
    background: linear-gradient(180deg, var(--dusk-top) 0%, var(--dusk-mid) 28%, #c24a3a 34%, var(--dusk-low) 55%, #6a4a66 75%, var(--dusk-deep) 100%);
  }
  .back__name {
    position: absolute;
    left: 0; right: 0;
    text-align: center;
    color: var(--white);
    font-size: 17px;
    letter-spacing: 3px;
    text-transform: uppercase;
  }
  .card--back-sea .back__name { top: 104px; }
  .card--back-beach .back__name { top: 298px; color: #dcdcf2; }
  .web-strip {
    position: absolute;
    left: 0; right: 0;
    top: 324px;
    height: 24px;
    background: rgba(120,120,130,0.55);
    color: var(--white);
    font-size: 14px;
    line-height: 24px;
    text-align: center;
  }
</style>
</head>
<body>

  <section class="card card--front-a front">
    <div class="front__band"><span class="front__name">Brightfold Chiropractic</span></div>
    <div class="front__info">
      <ul class="services">
        <li>Rehab</li><li>Sports Performance</li><li>Sports Injuries</li><li>Kinetic Tape</li><li>Soft Tissue Technique</li>
      </ul>
      <div class="rule"></div>
      <p class="address">2280 SW Harbor Loop<br>#210, Fairview, OR 97000</p>
      <div class="rule rule--second"></div>
      <p class="contact">555.014.2270<br>www.brightfoldchiro.example<br>drlane@brightfoldchiro.example</p>
    </div>
  </section>

  <section class="card card--back-sea">
    <div class="photo photo--sea" role="img" aria-label="Photo of a sunset over the ocean with glowing clouds"></div>
    <p class="back__name">Brightfold Chiropractic</p>
    <p class="web-strip">www.brightfoldchiro.example</p>
  </section>

  <section class="card card--back-beach">
    <div class="photo photo--beach" role="img" aria-label="Photo of two people silhouetted against a sunset on reflective wet sand, one standing and one leaping"></div>
    <p class="back__name">Brightfold Chiropractic</p>
  </section>

  <section class="card card--front-b front">
    <div class="front__band"><span class="front__name">Brightfold Chiropractic</span></div>
    <div class="front__info">
      <ul class="services">
        <li>Rehab</li><li>Sports Performance</li><li>Sports Injuries</li><li>Kinetic Tape</li><li>Soft Tissue Technique</li>
      </ul>
      <div class="rule"></div>
      <p class="address">2280 SW Harbor Loop<br>#210, Fairview, OR 97000</p>
      <div class="rule rule--second"></div>
      <p class="contact">555.014.2270<br>www.brightfoldchiro.example<br>drlane@brightfoldchiro.example</p>
    </div>
  </section>

</body>
</html>
```